Business Card Design for Fashion Tech Startup

Dear designers, we need a business card for Asia's premier fashion tech startup.!

PebbleHop is discovery e-commerce destination for busy, discerning parents in Asia featuring leading independent designers of baby, kids fashion apparel and sustainable brands from around the world.

PebbleHop is a modern, contemporary fashion tech startup targeting well-educated, well travelled and affluent parents. We're NOT your typical kiddy store!! Our design philosophy & e-commerce site is more like Vask.com, Orimesa.com, Pondwick.com, Farthollow.com.
Updates

Hi, size of the business card should be 84mm X 55mm. Would appreciate some business card layouts in Portrait as added consideration, i fancy the idea of a Portrait business card. What's important is that the business card should pique the receiver's interest to log onto the website to learn more. Many thanks and love forward to the designs!

Target Market(s)

Though modern, classy in look, feel & positioning, PebbleHop does possess a cheeky, fun-loving personality as depicted by its logo and the segment it targets (baby, kids) though the key decision makers i.e primarily mums between 25-40 who are well educated/travelled, local & expatriates, internet/digitally savvy, mid-high income working mums.

Industry/Entity Type

E-Commerce

Requirements
Must have
• Name, designation, email, phone & mobile number.
Company url : www.pebblehop.sg
Slogan : Discovery e-commerce destination for discerning, busy parents
Nice to have
• Call to Action such as a Discount code offering 10% discount
or asking people to "Like" us on our Chatterly page/Chatterly URL

```html
<!DOCTYPE html>
<html lang="en">
<head>
<meta charset="utf-8">
<title>PebbleHop Business Card</title>
<link rel="stylesheet" href="https://fonts.googleapis.com/css2?family=Open+Sans:wght@400;600;700&display=swap">
<style>
  :root {
    --backdrop: #e9e6e2;
    --card-white: #ffffff;
    --card-blue: #3d5a6c;
    --bubble: #18323d;
    --coral: #e8705a;
    --ink: #2f4a5e;
    --rule: #b9c3ca;
    --faint: #f0efee;
    --shadow: rgba(0, 0, 0, 0.14);
  }
  * { box-sizing: border-box; margin: 0; padding: 0; }
  html, body {
    width: 900px;
    height: 1200px;
    overflow: hidden;
    background: var(--backdrop);
    font-family: "Open Sans", Arial, sans-serif;
  }
  .canvas {
    width: 900px;
    height: 1200px;
    display: flex;
    flex-direction: column;
    align-items: center;
    justify-content: center;
    gap: 90px;
  }
  .card {
    position: relative;
    width: 588px;
    height: 385px;
    border-radius: 3px;
    box-shadow: 0 10px 28px var(--shadow);
    overflow: hidden;
  }

  /* Front: contact side */
  .card--front {
    background: var(--card-white);
    color: var(--ink);
    text-align: center;
  }
  .card--front .watermark-disc {
    position: absolute;
    left: 50%;
    top: 50%;
    width: 300px;
    height: 300px;
    margin: -150px 0 0 -150px;
    border-radius: 50%;
    background: var(--faint);
  }
  .brand {
    position: relative;
    display: flex;
    align-items: center;
    justify-content: center;
    gap: 12px;
    margin-top: 40px;
  }
  .brand__dot {
    width: 38px;
    height: 38px;
    border-radius: 50%;
    background: var(--coral);
  }
  .brand__name {
    font-size: 30px;
    font-weight: 700;
    color: var(--coral);
    letter-spacing: 0.5px;
  }
  .contact {
    position: relative;
    margin-top: 30px;
    font-size: 14.5px;
    line-height: 1.45;
  }
  .contact__name {
    font-size: 18px;
    font-weight: 600;
    letter-spacing: 0.5px;
  }
  .contact__role { font-size: 14px; }
  .contact__rule {
    width: 70px;
    height: 1px;
    margin: 12px auto;
    background: var(--rule);
  }
  .social {
    position: relative;
    display: flex;
    justify-content: center;
    gap: 16px;
    margin-top: 14px;
    font-size: 12px;
    font-weight: 600;
    color: var(--ink);
  }
  .slogan {
    position: absolute;
    left: 0;
    right: 0;
    bottom: 22px;
    font-size: 11.5px;
    color: var(--coral);
  }

  /* Back: promotional side */
  .card--back { background: var(--card-blue); }
  .illustration {
    position: absolute;
    left: 160px;
    top: 48px;
    width: 290px;
    height: 290px;
    border-radius: 50%;
    background: radial-gradient(circle at 50% 45%, #ffffff 0 22%, #f2a493 38%, var(--coral) 70%, #c9654f 100%);
  }
  .illustration__label {
    position: absolute;
    left: 0;
    right: 0;
    top: 190px;
    text-align: center;
    font-size: 28px;
    font-weight: 700;
    color: var(--card-white);
  }
  .offer {
    position: absolute;
    left: 390px;
    top: 40px;
    width: 130px;
    height: 96px;
  }
  .offer__text {
    position: absolute;
    inset: 0;
    padding-top: 16px;
    text-align: center;
    color: var(--card-white);
  }
  .offer__value { font-size: 22px; font-weight: 700; line-height: 1.05; }
  .offer__label { font-size: 16px; line-height: 1.2; }
  .offer__note { font-size: 8px; font-style: normal; }
</style>
</head>
<body>
<main class="canvas">

  <section class="card card--front" aria-label="Business card, contact side">
    <div class="watermark-disc"></div>
    <div class="brand">
      <span class="brand__dot"></span>
      <span class="brand__name">PebbleHop</span>
    </div>
    <div class="contact">
      <p class="contact__name">MARA QUINT</p>
      <p class="contact__role">Director of Operations</p>
      <div class="contact__rule"></div>
      <p>+65 02-748-3390</p>
      <p>askus@pebblehop.sg</p>
      <p>www.pebblehop.asia</p>
    </div>
    <div class="social">
      <span>Linkroll</span>
      <span>Chirpa</span>
      <span>Chatterly</span>
    </div>
    <p class="slogan">Discovery e-commerce destination for discerning, busy parents</p>
  </section>

  <section class="card card--back" aria-label="Business card, promotional side">
    <div class="illustration" role="img" aria-label="Round cluster of playful baby and kids items in coral and white around the brand name">
      <p class="illustration__label">PebbleHop.sg</p>
    </div>
    <div class="offer">
      <svg width="130" height="96" viewBox="0 0 130 96" aria-hidden="true">
        <ellipse cx="65" cy="44" rx="62" ry="42" fill="var(--bubble)"/>
        <path d="M30 76 L18 95 L48 82 Z" fill="var(--bubble)"/>
      </svg>
      <div class="offer__text">
        <p class="offer__value">10%</p>
        <p class="offer__label">Discount</p>
        <p class="offer__note">*Conditions Apply</p>
      </div>
    </div>
  </section>

</main>
</body>
</html>
```